Corporate brochure

Design a corporate brochure based on our website www.drelvorn.com in both PDF and as a powerpoint presentation.

Color theme - white, blue and purple same as DRV Logo.

I attach some old brochures we have done but are not polished, as well as some logos.

```html
<!DOCTYPE html>
<html lang="en">
<head>
<meta charset="utf-8">
<title>Drelvorn – Trifold Brochure</title>
<link href="https://fonts.googleapis.com/css2?family=Open+Sans:ital,wght@0,400;0,600;0,700;0,800;1,400;1,700&display=swap" rel="stylesheet">
<style>
:root{
  --navy:#16143b;
  --navy-soft:#25215a;
  --plum:#4a1838;
  --magenta:#b0267a;
  --ink:#2a2a33;
  --paper:#ffffff;
  --stage:#dcdcdc;
  --black:#0b0b0d;
}
*{box-sizing:border-box;margin:0;padding:0}
html,body{width:713px;height:1200px;overflow:hidden}
body{background:var(--stage);font-family:"Open Sans",Arial,sans-serif;color:var(--ink);position:relative}
.spread{position:absolute;left:12px;width:689px;height:530px;display:flex;box-shadow:0 4px 14px rgba(0,0,0,.18)}
.spread--outside{top:40px}
.spread--inside{top:630px}
.panel{position:relative;width:229.67px;height:100%;background:var(--paper);overflow:hidden}
.photo{position:absolute;left:0;width:100%}
.heading-bar{border-left:3px solid var(--magenta);padding-left:6px;font-weight:800;color:var(--navy);text-transform:uppercase;line-height:1.12}
.body-copy{font-size:6.6px;line-height:1.5}
.list{font-size:6.4px;line-height:1.55;padding-left:12px}

/* About panel */
.about{padding:22px 18px 0}
.about__title{font-size:15px;font-weight:700;font-style:italic;color:var(--ink);text-transform:none;margin-bottom:8px}
.about__text{font-style:italic;font-size:6.8px;line-height:1.5}
.about__rule{width:70px;height:1.5px;background:var(--magenta);margin:12px 0 8px}
.about__lead{font-style:italic;font-weight:700;font-size:7px;line-height:1.45}
.about .photo{top:340px;height:190px;background:linear-gradient(135deg,#4b3a7a,#b85a8f 45%,#7a5a5a 70%,#3a3460)}

/* Back panel */
.back{background:var(--navy);color:#fff;text-align:center}
.back .photo{top:0;height:150px;background:linear-gradient(180deg,#2e2a66,var(--navy))}
.back__box{position:absolute;top:95px;left:18px;right:18px;border:1px solid rgba(255,255,255,.45);border-radius:14px;padding:10px 10px;font-size:6.4px;line-height:1.5;font-style:italic}
.brand{display:flex;align-items:center;justify-content:center;gap:6px;font-weight:700;letter-spacing:.3px}
.brand__dot{width:14px;height:14px;border-radius:50%;background:var(--magenta)}
.back .brand{position:absolute;top:200px;left:0;right:0;font-size:17px}
.contact{position:absolute;top:248px;left:0;right:0;font-size:8.6px;line-height:1.4}
.contact__item{margin-bottom:9px}
.contact__icon{display:block;margin:0 auto 3px}
.partner{position:absolute;bottom:22px;left:0;right:0;display:flex;justify-content:center;align-items:center;gap:6px;font-size:10px;font-weight:700}
.partner__mark{width:14px;height:14px;background:#fff}

/* Cover */
.cover__band{position:absolute;top:0;left:0;right:0;height:58px;background:var(--black);color:#fff}
.cover__band .brand{height:100%;font-size:20px}
.cover__tag{position:absolute;top:40px;left:0;right:0;text-align:center;font-size:5px;color:#ddd}
.cover__title{position:absolute;top:72px;left:14px;right:14px;text-align:center;color:var(--plum);font-weight:800;font-size:19px;line-height:1.05;text-transform:uppercase}
.cover .photo{top:178px;height:262px;background:linear-gradient(160deg,#bfc6cc,#e3c23a 40%,#d9a81a 60%,#2e5fb0 85%)}
.cover__strip{position:absolute;top:408px;left:0;right:0;height:82px;background:var(--navy);color:#fff;text-align:center;font-size:8.6px;line-height:1.4;padding:16px 14px 0}
.cover__url{position:absolute;bottom:12px;left:0;right:0;text-align:center;font-size:10px;color:var(--ink)}

/* Inside */
.inside-pad{position:absolute;left:18px;right:14px}
.services .photo{top:0;height:80px;background:linear-gradient(120deg,#c77a3a,#3b4c7a 60%,#1f2a4f)}
.services__head{top:96px;font-size:9.5px}
.services__list{top:146px}
.industries{top:252px}
.industries__title{font-size:16px;font-weight:700;color:var(--navy);border-left:3px solid var(--magenta);padding-left:6px}
.industries__sub{font-size:6px;margin:2px 0 12px 9px}
.industries__grid{display:grid;grid-template-columns:1fr 1fr;row-gap:18px;column-gap:6px}
.industry{display:flex;align-items:center;gap:6px;font-size:6.8px;line-height:1.2}
.industry__icon{width:18px;height:18px;border-radius:50%;background:var(--navy);flex:none;display:flex;align-items:center;justify-content:center}
.industry__icon::after{content:"";width:6px;height:6px;border-radius:50%;border:1.4px solid #fff}

.trade .photo{top:0;height:92px;background:linear-gradient(135deg,#1a2238,#3f5a78 50%,#0f1626)}
.trade__head{top:108px;font-size:10px}
.trade__text{top:140px}
.logistics .photo--top{top:0;height:92px;background:linear-gradient(120deg,#2a3a5a,#c7d0dc 45%,#d8742f 80%,#6b3a2a)}
.logistics__head{top:108px;font-size:9.5px}
.logistics__text{top:152px}
.refinery{position:absolute;left:229.67px;bottom:0;width:459.33px;height:190px;background:linear-gradient(180deg,rgba(255,255,255,0),#e8b888 35%,#8b8fa8 70%,#3a4058)}
</style>
</head>
<body>

<section class="spread spread--outside">
  <article class="panel about">
    <h2 class="heading-bar about__title">About us</h2>
    <p class="about__text">We represent leading global manufacturers, from more than 40 countries around the world as well a major supplier of core chemistries such as lithium, magnesium, potassium and specialty silicon performance materials and additives. We are big enough to supply some of the largest industrial customers in the world, yet small enough to care about each and every shipment that bears our name – from importing &amp; exporting, bulk material handling &amp; processing, toll manufacturing &amp; packing services to logistics and warehousing.</p>
    <div class="about__rule"></div>
    <p class="about__lead">As a leading supplier of LITHIUM, SILICA, MAGNESIUM, and POTASSIUM specialty and fine chemicals, we offer an extensive lineup of ingredients and derivatives.</p>
    <div class="photo" role="img" aria-label="Collage of industry photos: construction materials, paint and coatings, grease and lubricants, plastics and rubber, oil and gas, wood preservation"></div>
  </article>

  <article class="panel back">
    <div class="photo" role="img" aria-label="Faint molecular structure background"></div>
    <p class="back__box">We are a chemical trader, ingredient and raw material distributor and technology development company specializing in bulk materials, performance specialty chemicals and intermediates with leading positions in lithium, magnesium, silica and potassium chemistries.</p>
    <div class="brand"><span class="brand__dot"></span>drelvorn</div>
    <div class="contact">
      <div class="contact__item">
        <svg class="contact__icon" width="8" height="10" viewBox="0 0 8 10"><path d="M4 0a3.5 3.5 0 0 0-3.5 3.5C.5 6 4 10 4 10s3.5-4 3.5-6.5A3.5 3.5 0 0 0 4 0z" fill="var(--magenta)"/><circle cx="4" cy="3.5" r="1.3" fill="#fff"/></svg>
        Drelvorn, LLC.<br>418 Harlow Ave. | Bldg 12 |<br>Marston, FL 32011 | United States
      </div>
      <div class="contact__item">
        <svg class="contact__icon" width="9" height="9" viewBox="0 0 10 10"><circle cx="5" cy="5" r="5" fill="var(--magenta)"/><rect x="3" y="2.5" width="4" height="5" rx=".6" fill="#fff"/></svg>
        555.210.4837
      </div>
      <div class="contact__item">
        <svg class="contact__icon" width="9" height="9" viewBox="0 0 10 10"><circle cx="5" cy="5" r="5" fill="var(--magenta)"/><path d="M3 3l1 0 .6 1.4-.7.6a4 4 0 0 0 1.6 1.6l.6-.7L7 6.5v1C5 7.6 2.6 5.2 3 3z" fill="#fff"/></svg>
        555.210.4890
      </div>
      <div class="contact__item">
        <svg class="contact__icon" width="9" height="9" viewBox="0 0 10 10"><circle cx="5" cy="5" r="5" fill="var(--magenta)"/><circle cx="5" cy="5" r="2.6" fill="none" stroke="#fff" stroke-width=".8"/><path d="M2.4 5h5.2M5 2.4v5.2" stroke="#fff" stroke-width=".6"/></svg>
        www.drelvorn.com
      </div>
    </div>
    <div class="partner"><span class="partner__mark"></span>Northvale Salts Co.</div>
  </article>

  <article class="panel cover">
    <header class="cover__band"><div class="brand"><span class="brand__dot"></span>drelvorn</div></header>
    <p class="cover__tag">Bulk Chemicals &amp; Specialty Performance Materials</p>
    <h1 class="cover__title">Bulk Chemicals<br>&amp; Specialty<br>Performance<br>Material</h1>
    <div class="photo" role="img" aria-label="Worker in yellow protective suit beside a blue chemical drum at an industrial plant"></div>
    <p class="cover__strip">Experts in raw material supply and a proven history of innovating products as a materials science company.</p>
    <p class="cover__url">www.drelvorn.com</p>
  </article>
</section>

<section class="spread spread--inside">
  <article class="panel services">
    <div class="photo" role="img" aria-label="Laboratory technician working with samples"></div>
    <h2 class="inside-pad heading-bar services__head">Custom Services -<br>Mixing, Blending<br>Formulation and Packaging</h2>
    <ol class="inside-pad list services__list">
      <li>Chemical repackaging and filling</li>
      <li>Toll blending / toll manufacturing</li>
      <li>Private labeling and branding</li>
      <li>Bulk Blending Solutions (converting powder to liquid products for commodities that need conversion for transport - tanker, iso, totes or drums).</li>
    </ol>
    <div class="inside-pad industries">
      <h2 class="industries__title">Industries</h2>
      <p class="industries__sub">Markets we serve and an extensive portfolio of technologies and solutions we provide.</p>
      <div class="industries__grid">
        <div class="industry"><span class="industry__icon"></span>Oil<br>&amp; Gas</div>
        <div class="industry"><span class="industry__icon"></span>Paint<br>&amp; Coatings</div>
        <div class="industry"><span class="industry__icon"></span>Glass, Glazes<br>&amp; Ceramics</div>
        <div class="industry"><span class="industry__icon"></span>Plastics, PVC,<br>Rubber &amp; Foam</div>
        <div class="industry"><span class="industry__icon"></span>Grease &amp;<br>Lubricant Additives</div>
        <div class="industry"><span class="industry__icon"></span>Refractories Wood<br>Preservation Additives</div>
      </div>
    </div>
  </article>

  <article class="panel trade">
    <div class="photo" role="img" aria-label="Aerial view of a container ship at sea"></div>
    <h2 class="inside-pad heading-bar trade__head">Importing<br>Exporting</h2>
    <div class="inside-pad trade__text">
      <p class="body-copy">Expertise in importing / exporting materials goes far beyond moving materials from one dock to the next, it requires the "know-how" and the "how" of doing it.</p>
      <p class="body-copy" style="margin-top:6px">As global trade experts we are experienced in the materials, procedures and regulations offerings a truly integrated structure that allows us all to benefit from established long-term supply relationships across the wider network for Asia Pacific Oceania Middle East and Europe and our customers with our</p>
      <ol class="list" style="margin-top:8px">
        <li>Take over the responsibility of shipping various types of chemicals (including hazmat)</li>
        <li>Coordination and timely export of shipments</li>
        <li>Managing the administrative burden of import rules and regulations.</li>
        <li>Extensive experience with CBP procedures</li>
        <li>Firm knowledge of FDA, EPA, DEA requirements</li>
        <li>Strict compliance with hazmat DOT regulations</li>
      </ol>
    </div>
  </article>

  <article class="panel logistics">
    <div class="photo photo--top" role="img" aria-label="Truck on a highway at sunset with motion blur"></div>
    <h2 class="inside-pad heading-bar logistics__head">Bulk Terminals,<br>Warehousing,<br>Distribution &amp; Logistics</h2>
    <div class="inside-pad logistics__text">
      <p class="body-copy">From break bulk, silos, tankers, containers to less-than truck-loads quantities, we aim to fulfill our customers' needs no matter the circumstances. We offer complete intermodal logistics support for direct container deliveries from seaport or rail head, as well as local distribution from warehouses in proximity to our customers.</p>
      <ol class="list" style="margin-top:8px">
        <li>Bulk packaging (drums, totes, ISO tanks, etc.)</li>
        <li>FCL deliveries from port or LTL from warehouse</li>
        <li>Intermodal freight options via truck, rail or air.</li>
      </ol>
    </div>
  </article>

  <div class="refinery" role="img" aria-label="Refinery and power plant at dusk"></div>
</section>

</body>
</html>
```